Quiet Ledger needs a book cover

Enabling people to find a new way of looking at money. If peoples thoughts, attitude and emotions around money are not inline with their goals and dreams then it is often harder to achieve their version of success.

Recognition that we have an emotional and a practical way with money.

Quiet Ledger enables people to find a sustainable (balanced) way with money for their life right now and their future.

Developing this over the years and seeing clients achieve a clear picture/idea/thought connection that is positive around money and it's purpose to them in their lives has truly been fabulous as they have then gone on to achieve their goals and dreams.

Title of book = Quiet Ledger
Tag line = Being healthy being wealthy
Authors Name = Ruth Pell
Book Size = 135 width x 185 height
Thumbnail = Cover must work well as well as full size
Looking for simple and clear app-able / icon type image
Feel free to have fun with it
A simple yet refreshing balanced, eye-catching design.

The back will include authors photo, blurb, testimonials, barcode, ISBN number & price. I will provide once front cover is sorted.
Updates

Project Deadline Extended
Reason: Realised that the tag line for the book was incorrect.

Target Market(s)

Individuals

Industry/Entity Type

Work

Requirements
Must have
• First work on front cover, once approved we can then do spine and back cover
Should not have

```html
<!DOCTYPE html>
<html lang="en">
<head>
<meta charset="utf-8">
<title>Quiet Ledger – Book Cover</title>
<link href="https://fonts.googleapis.com/css2?family=Montserrat:wght@700&family=Questrial&display=swap" rel="stylesheet">
<style>
  :root {
    --backdrop: #e9e6e1;
    --cover-grey: #dcdcdc;
    --cover-grey-light: #e6e6e6;
    --pink: #e8338f;
    --white: #ffffff;
    --ink: #1a1a1a;
    --pocket-line: #3a3a3a;
    --tie-green: #4e9a2a;
    --tie-navy: #1d2a44;
    --bill-grey: #c9c9bf;
    --bill-dark: #7d7f76;
  }
  html, body {
    margin: 0;
    padding: 0;
    width: 1085px;
    height: 1200px;
    overflow: hidden;
    background: var(--backdrop);
  }
  .canvas {
    position: relative;
    width: 1085px;
    height: 1200px;
  }
  .book-cover {
    position: absolute;
    left: 170px;
    top: 95px;
    width: 745px;
    height: 1010px;
    background: linear-gradient(135deg, var(--cover-grey-light), var(--cover-grey));
    overflow: hidden;
    box-shadow: 0 6px 18px rgba(0,0,0,0.25);
  }
  .tie {
    position: absolute;
    left: 0;
    top: 0;
    width: 150px;
    height: 1010px;
    background: linear-gradient(90deg, var(--tie-navy) 0%, var(--tie-green) 35%, #5aa832 70%, var(--tie-navy) 100%);
    border-radius: 0 40px 40px 0 / 0 500px 500px 0;
    box-shadow: 3px 0 6px rgba(0,0,0,0.3);
  }
  .banknotes {
    position: absolute;
    left: 185px;
    top: 62px;
    width: 500px;
    height: 160px;
    background: linear-gradient(180deg, var(--bill-grey), var(--bill-dark));
    clip-path: polygon(0 22%, 30% 8%, 55% 0, 80% 6%, 100% 22%, 100% 100%, 0 100%);
  }
  .pocket {
    position: absolute;
    left: 0;
    top: 0;
    width: 745px;
    height: 1010px;
  }
  .title-tab {
    position: absolute;
    left: 285px;
    top: 162px;
    width: 325px;
    height: 80px;
    background: var(--pink);
    border-radius: 40px 40px 0 0;
  }
  .title-band {
    position: absolute;
    left: 165px;
    top: 225px;
    width: 545px;
    height: 137px;
    background: var(--pink);
  }
  .title {
    position: absolute;
    left: 165px;
    top: 178px;
    width: 545px;
    margin: 0;
    text-align: center;
    color: var(--white);
    font-family: "Montserrat", sans-serif;
    font-weight: 700;
    line-height: 1;
  }
  .title-top {
    display: block;
    font-size: 46px;
  }
  .title-bottom {
    display: block;
    font-size: 82px;
    margin-top: 6px;
  }
  .question {
    position: absolute;
    left: 290px;
    top: 385px;
    width: 300px;
    margin: 0;
    color: var(--ink);
    font-family: "Questrial", sans-serif;
    font-weight: 400;
    text-align: center;
    line-height: 0.95;
  }
  .question span { display: block; }
  .q-plain { font-size: 40px; }
  .q-small { font-size: 32px; }
  .q-strong { font-size: 58px; font-style: italic; }
  .q-line-1 { padding-left: 26px; }
  .q-line-3 { padding-left: 14px; }
  .q-line-4 { padding-left: 10px; }
  .q-line-5 { padding-left: 0; }
  .q-line-6 { padding-left: 120px; font-size: 48px; }
  .author-band {
    position: absolute;
    left: 185px;
    top: 670px;
    width: 505px;
    height: 72px;
    background: var(--pink);
    color: var(--white);
    font-family: "Montserrat", sans-serif;
    font-weight: 700;
    font-size: 44px;
    line-height: 72px;
    text-align: center;
  }
</style>
</head>
<body>
<div class="canvas">
  <div class="book-cover">
    <div class="tie" role="img" aria-label="Photograph of a green and navy striped necktie running down the left edge"></div>
    <div class="banknotes" role="img" aria-label="Photograph of fanned dollar banknotes tucked into a shirt pocket"></div>
    <svg class="pocket" viewBox="0 0 745 1010" aria-hidden="true">
      <path d="M185 218 L185 790 Q446 830 708 790 L708 218" fill="none" stroke="var(--pocket-line)" stroke-width="2"/>
      <path d="M195 218 L195 782" fill="none" stroke="var(--pocket-line)" stroke-width="1" opacity="0.5"/>
      <path d="M698 218 L698 782" fill="none" stroke="var(--pocket-line)" stroke-width="1" opacity="0.5"/>
    </svg>
    <div class="title-tab"></div>
    <div class="title-band"></div>
    <h1 class="title">
      <span class="title-top">Quiet</span>
      <span class="title-bottom">Ledger</span>
    </h1>
    <p class="question">
      <span class="q-plain q-line-1">What is the</span>
      <span class="q-strong q-line-2">purpose</span>
      <span class="q-small q-line-3">of</span>
      <span class="q-strong q-line-4">money</span>
      <span class="q-small q-line-5">in your</span>
      <span class="q-strong q-line-6">life?</span>
    </p>
    <div class="author-band">Ruth Pell</div>
  </div>
</div>
</body>
</html>
```